Business Card Design Harbor of Calm

mental health provider
contemporary
warmth
inviting

Target Market(s)

mental health clients adults

Industry/Entity Type

Mental Health

Contact Information for Business Card

Danielle Korrish PMHNP
2938 SW Fennick Ave
Suite 340C
Portland OR 97225
Fax 503-418-9152
Tel 503-418-9267
Email danielle@dkorrish.com
Website dkorrish.com

Requirements
Nice to have
• see above
Should not have
• no medical logos

```html
<!DOCTYPE html>
<html lang="en">
<head>
<meta charset="utf-8">
<title>Danielle Korrish PMHNP – Business Card</title>
<link rel="stylesheet" href="https://fonts.googleapis.com/css2?family=Alegreya:ital,wght@0,500;1,700&family=Lato:wght@400;700&display=swap">
<style>
  :root {
    --canvas-bg: #c9c9c9;
    --card-brown: #2e2216;
    --leaf-green: #b9d87f;
    --band-stripe: #a9c96c;
    --band-fill: #d6eaa9;
    --shadow: rgba(0,0,0,0.35);
  }
  * { margin: 0; padding: 0; box-sizing: border-box; }
  html, body { width: 1200px; height: 1000px; overflow: hidden; }
  body {
    background: var(--canvas-bg);
    position: relative;
    font-family: "Lato", sans-serif;
    color: var(--leaf-green);
  }
  .card {
    position: absolute;
    width: 620px;
    height: 354px;
    background: var(--card-brown);
    box-shadow: 0 12px 28px var(--shadow);
    overflow: hidden;
  }
  .card--front { left: 70px; top: 80px; }
  .card--back { left: 510px; top: 540px; }
  .card__band {
    position: absolute;
    left: 0; right: 0; bottom: 0;
    height: 50px;
    border-top: 9px solid var(--band-stripe);
    background: linear-gradient(180deg, var(--band-fill), #cfe59d);
  }
  /* front */
  .front__mark {
    position: absolute;
    left: 0; right: 0; top: 62px;
    text-align: center;
  }
  .front__badge {
    display: block;
    width: 46px; height: 46px;
    border-radius: 50%;
    background: var(--leaf-green);
    margin: 0 auto 6px -130px;
    position: relative;
    left: 50%;
  }
  .front__name {
    font-family: "Alegreya", serif;
    font-weight: 500;
    font-size: 54px;
    line-height: 1;
    letter-spacing: 0.5px;
  }
  .front__title {
    font-family: "Lato", sans-serif;
    font-size: 27px;
    margin-top: 4px;
    padding-left: 90px;
    letter-spacing: 0.5px;
  }
  .front__contact {
    position: absolute;
    left: 0; right: 0; top: 228px;
    text-align: center;
    font-size: 21px;
    line-height: 1.35;
    padding-left: 120px;
  }
  /* back */
  .back__name {
    position: absolute;
    left: 0; right: 0; top: 34px;
    text-align: center;
    font-family: "Alegreya", serif;
    font-style: italic;
    font-weight: 700;
    font-size: 36px;
  }
  .back__title {
    position: absolute;
    left: 0; right: 0; top: 80px;
    text-align: center;
    font-size: 18px;
    letter-spacing: 0.5px;
  }
  .back__phones {
    position: absolute;
    left: 0; right: 0; top: 134px;
    text-align: center;
    font-size: 21px;
    line-height: 1.4;
  }
  .back__label { font-weight: 700; }
  .back__address {
    position: absolute;
    left: 0; right: 0; top: 220px;
    text-align: center;
    font-size: 23px;
    line-height: 1.4;
  }
</style>
</head>
<body>
  <section class="card card--front" aria-label="Business card front">
    <div class="front__mark">
      <span class="front__badge" aria-hidden="true"></span>
      <div class="front__name">Danielle Korrish</div>
      <div class="front__title">PMHNP, Inc.</div>
    </div>
    <div class="front__contact">
      <div>danielle@dkorrish.com</div>
      <div>www.dkorrish.com</div>
    </div>
    <div class="card__band" role="img" aria-label="Pale green band with a soft decorative pattern"></div>
  </section>

  <section class="card card--back" aria-label="Business card back">
    <div class="back__name">Danielle Korrish</div>
    <div class="back__title">PMHNP</div>
    <div class="back__phones">
      <div><span class="back__label">Fax:</span> 503-418-9152</div>
      <div><span class="back__label">Phone:</span> 503-418-9267</div>
    </div>
    <div class="back__address">
      <div>2938 SW Fennick Ave Suite</div>
      <div>340C Portland OR 97225</div>
    </div>
    <div class="card__band" role="img" aria-label="Pale green band with a soft decorative pattern"></div>
  </section>
</body>
</html>
```